Vantora plinth system based website for technology jobs website

We need a website design for a technology job listing website, mainly aiming at 20/30/40 year old nerds. Jobs listed from multiple sources will be concatenated and organised. This website will be built with Vantora plinth system (https://plinthkit.example/manual/) so please use their components. The design should be simple and clear, so a user can directly look for offerings that are interesting for him.

Three different pages will be needed:

1. Main jobs list page

Contains a large table (https://plinthkit.example/manual/parts/grid-views.html#grid-views-anatomy), on top or next to this data-table users should be able to apply filters (select countries, select salary ranges) and somewhere an overview of the selected filters should be shown.

- A subscribe bar should be shown somewhere to allow a user to register for weekly/monthly mailings for new job offers with his preferred search filters.

2. Selected item page

If an item is clicked, a user should be able to view a job posting and it's details.

3. An advertiser should be able post his job offer.
Similar fields as https://post.ledgerworkboard.example/.
(https://plinthkit.example/manual/parts/input-boxes.html#input-boxes-arrangement)

Target Market(s)

20/30/40 year old nerds.

Industry/Entity Type

Computer

Logo Text

QuarkHire.io

Number of Pages Required

3 page

Colors

Designer to choose colors to be used in the design.

Requirements
Must have
• 1. Main jobs list page
• Contains a large table (https://plinthkit.example/manual/parts/grid-views.html#grid-views-anatomy), on top or next to this data-table users should be able to apply filters (select countries, select salary ranges) and somewhere an overview of the selected filters should be shown.
• - A subscribe bar should be shown somewhere to allow a user to register for weekly/monthly mailings for new job offers with his preferred search filters.
• 2. Selected item page
• If an item is clicked, a user should be able to view a job posting and it's details.
• 3. An advertiser should be able post his job offer,
• (https://plinthkit.example/manual/parts/input-boxes.html#input-boxes-arrangement)
• Please use open fonts!

```html
<!DOCTYPE html>
<html lang="en">
<head>
<meta charset="utf-8">
<title>QuarkHire.io – Job Listings</title>
<link href="https://fonts.googleapis.com/css2?family=Roboto:wght@400;500&display=swap" rel="stylesheet">
<style>
  :root {
    --page-bg: #f0f0f0;
    --hero-dark: #07162c;
    --hero-mid: #0b3a6e;
    --search-band: #03a9f4;
    --search-btn: #0d5394;
    --card-bg: #ffffff;
    --row-alt: #f5f5f5;
    --rule: #e6e6e6;
    --link: #039be5;
    --head-text: #2a2a2a;
    --cell-text: #666666;
    --field-text: #8a8a8a;
    --chip-bg: #e1f5fe;
    --footer-bg: #303237;
    --footer-text: #ffffff;
    --fab: #dc3d2c;
  }
  * { box-sizing: border-box; margin: 0; padding: 0; }
  html, body { width: 1200px; height: 1086px; overflow: hidden; }
  body {
    position: relative;
    background: var(--page-bg);
    font-family: "Roboto", Arial, sans-serif;
  }
  .hero-backdrop {
    position: absolute; left: 0; top: 0; width: 1200px; height: 398px;
    background: radial-gradient(ellipse at 35% 55%, #1a5d9e 0%, var(--hero-mid) 35%, var(--hero-dark) 85%);
  }
  .menu-toggle { position: absolute; left: 86px; top: 23px; }
  .brand {
    position: absolute; left: 0; top: 16px; width: 1200px; text-align: center;
    color: #fff; font-size: 31px; font-weight: 500; letter-spacing: 0.2px;
  }
  .search-band {
    position: absolute; left: 86px; top: 105px; width: 1028px; height: 98px;
    background: var(--search-band);
  }
  .field {
    position: absolute; top: 29px; height: 41px; background: #fff; border-radius: 2px;
    display: flex; align-items: center; justify-content: space-between;
    padding: 0 8px 0 7px; font-size: 12.5px; color: var(--field-text);
  }
  .field-keyword { left: 30px; width: 292px; }
  .field-location { left: 330px; width: 215px; }
  .field-salary { left: 554px; width: 213px; }
  .field-designation { left: 776px; width: 113px; }
  .search-button {
    position: absolute; left: 898px; top: 29px; width: 101px; height: 41px;
    background: var(--search-btn); border-radius: 2px;
    display: flex; align-items: center; justify-content: center;
  }
  .job-table {
    position: absolute; left: 84px; top: 267px; width: 1032px; height: 729px;
    background: var(--card-bg); box-shadow: 0 1px 3px rgba(0,0,0,0.18);
    padding-top: 33px;
  }
  .active-filters {
    position: absolute; left: 15px; top: 7px; display: flex; align-items: center; gap: 6px;
    font-size: 11.5px; color: var(--cell-text);
  }
  .chip {
    height: 20px; padding: 0 9px; border-radius: 10px; background: var(--chip-bg);
    color: var(--link); display: inline-flex; align-items: center;
  }
  .row {
    display: grid; grid-template-columns: 228px 185px 163px 137px 150px 1fr;
    align-items: center; padding-left: 15px; height: 50px;
    border-bottom: 1px solid var(--rule); font-size: 12.5px; color: var(--cell-text);
  }
  .row.head { height: 48px; color: var(--head-text); font-size: 12.8px; border-bottom-color: #dcdcdc; }
  .row.selected { background: var(--row-alt); }
  .job-title { display: flex; align-items: center; gap: 7px; color: var(--link); font-weight: 500; }
  .row.head .job-title { font-weight: 400; }
  .check {
    width: 13px; height: 13px; border: 1px solid #8c8c8c; border-radius: 2px; background: #fff;
    display: inline-flex; align-items: center; justify-content: center; flex: none;
  }
  .skills { display: inline-flex; align-items: center; gap: 3px; }
  .subscribe-bar {
    position: absolute; left: 15px; right: 15px; bottom: 8px; height: 34px;
    display: flex; align-items: center; gap: 10px; font-size: 12.5px; color: var(--head-text);
  }
  .subscribe-email {
    width: 260px; height: 30px; border: 1px solid #d6d6d6; border-radius: 2px;
    display: flex; align-items: center; padding: 0 8px; color: var(--field-text);
  }
  .frequency { display: inline-flex; align-items: center; gap: 5px; color: var(--cell-text); }
  .radio { width: 12px; height: 12px; border: 1px solid #8c8c8c; border-radius: 50%; display: inline-flex; align-items: center; justify-content: center; }
  .radio.on::after { content: ""; width: 6px; height: 6px; border-radius: 50%; background: var(--link); }
  .subscribe-button {
    height: 30px; padding: 0 16px; background: var(--search-btn); color: #fff; border-radius: 2px;
    display: inline-flex; align-items: center; font-weight: 500; font-size: 12px; letter-spacing: 0.4px;
  }
  .add-button {
    position: absolute; left: 1128px; top: 936px; width: 60px; height: 60px; border-radius: 50%;
    background: var(--fab); display: flex; align-items: center; justify-content: center;
    box-shadow: 0 2px 5px rgba(0,0,0,0.25);
  }
  .site-footer {
    position: absolute; left: 0; top: 1045px; width: 1200px; height: 41px;
    background: var(--footer-bg); color: var(--footer-text);
    display: flex; align-items: center; justify-content: center; font-size: 12px;
  }
</style>
</head>
<body>
  <div class="hero-backdrop" role="img" aria-label="Dark blue background of glowing connected network lines"></div>

  <svg class="menu-toggle" width="24" height="18" viewBox="0 0 24 18" aria-label="Menu">
    <rect y="1" width="24" height="2.4" fill="#fff"/>
    <rect y="7.8" width="24" height="2.4" fill="#fff"/>
    <rect y="14.6" width="24" height="2.4" fill="#fff"/>
  </svg>
  <div class="brand">QuarkHire.io</div>

  <form class="search-band">
    <div class="field field-keyword"><span>Keyword e.g. ( jobTitle, Description,Tags)</span>
      <svg width="9" height="6" viewBox="0 0 9 6"><path d="M1 1l3.5 3.5L8 1" fill="none" stroke="#999" stroke-width="1.2"/></svg></div>
    <div class="field field-location"><span>Select Location</span>
      <svg width="9" height="6" viewBox="0 0 9 6"><path d="M1 1l3.5 3.5L8 1" fill="none" stroke="#999" stroke-width="1.2"/></svg></div>
    <div class="field field-salary"><span>Salary</span>
      <svg width="9" height="6" viewBox="0 0 9 6"><path d="M1 1l3.5 3.5L8 1" fill="none" stroke="#999" stroke-width="1.2"/></svg></div>
    <div class="field field-designation"><span>Designation</span>
      <svg width="9" height="6" viewBox="0 0 9 6"><path d="M1 1l3.5 3.5L8 1" fill="none" stroke="#999" stroke-width="1.2"/></svg></div>
    <div class="search-button" aria-label="Search">
      <svg width="21" height="21" viewBox="0 0 21 21"><circle cx="8.5" cy="8.5" r="6.3" fill="none" stroke="#fff" stroke-width="3"/><path d="M13.2 13.2l5.6 5.6" stroke="#fff" stroke-width="3.4" stroke-linecap="round"/></svg>
    </div>
  </form>

  <section class="job-table">
    <div class="active-filters">
      <span>Selected filters:</span>
      <span class="chip">Any location</span>
      <span class="chip">Any salary</span>
      <span class="chip">Full Time</span>
    </div>
    <div class="row head">
      <div class="job-title"><span class="check"></span>Job Type</div>
      <div>Country Name</div><div>Experience</div><div>Salary</div><div>Keyskills</div><div>Employment Type</div>
    </div>
    <div class="row"><div class="job-title"><span class="check"></span>Software Engineer</div><div>Country</div><div>0 -1</div><div>$ 20000</div><div class="skills">HTML Javascript <svg width="8" height="5" viewBox="0 0 8 5"><path d="M1 1l3 3 3-3" fill="none" stroke="#888"/></svg></div><div>Full Time</div></div>
    <div class="row selected"><div class="job-title"><span class="check"><svg width="9" height="8" viewBox="0 0 9 8"><path d="M1 4l2.5 2.5L8 1" fill="none" stroke="#888" stroke-width="1.3"/></svg></span>Software Engineer</div><div>Country</div><div>0 -1</div><div>$ 20000</div><div class="skills">HTML Javascript <svg width="8" height="5" viewBox="0 0 8 5"><path d="M1 1l3 3 3-3" fill="none" stroke="#888"/></svg></div><div>Full Time</div></div>
    <div class="row"><div class="job-title"><span class="check"></span>Software Engineer</div><div>Country</div><div>0 -1</div><div>$ 20000</div><div class="skills">HTML Javascript <svg width="8" height="5" viewBox="0 0 8 5"><path d="M1 1l3 3 3-3" fill="none" stroke="#888"/></svg></div><div>Full Time</div></div>
    <div class="row"><div class="job-title"><span class="check"></span>Software Engineer</div><div>Country</div><div>0 -1</div><div>$ 20000</div><div class="skills">HTML Javascript <svg width="8" height="5" viewBox="0 0 8 5"><path d="M1 1l3 3 3-3" fill="none" stroke="#888"/></svg></div><div>Full Time</div></div>
    <div class="row"><div class="job-title"><span class="check"></span>Software Engineer</div><div>Country</div><div>0 -1</div><div>$ 20000</div><div class="skills">HTML Javascript <svg width="8" height="5" viewBox="0 0 8 5"><path d="M1 1l3 3 3-3" fill="none" stroke="#888"/></svg></div><div>Full Time</div></div>
    <div class="row"><div class="job-title"><span class="check"></span>Software Engineer</div><div>Country</div><div>0 -1</div><div>$ 20000</div><div class="skills">HTML Javascript <svg width="8" height="5" viewBox="0 0 8 5"><path d="M1 1l3 3 3-3" fill="none" stroke="#888"/></svg></div><div>Full Time</div></div>
    <div class="row"><div class="job-title"><span class="check"></span>Software Engineer</div><div>Country</div><div>0 -1</div><div>$ 20000</div><div class="skills">HTML Javascript <svg width="8" height="5" viewBox="0 0 8 5"><path d="M1 1l3 3 3-3" fill="none" stroke="#888"/></svg></div><div>Full Time</div></div>
    <div class="row"><div class="job-title"><span class="check"></span>Software Engineer</div><div>Country</div><div>0 -1</div><div>$ 20000</div><div class="skills">HTML Javascript <svg width="8" height="5" viewBox="0 0 8 5"><path d="M1 1l3 3 3-3" fill="none" stroke="#888"/></svg></div><div>Full Time</div></div>
    <div class="row"><div class="job-title"><span class="check"></span>Software Engineer</div><div>Country</div><div>0 -1</div><div>$ 20000</div><div class="skills">HTML Javascript <svg width="8" height="5" viewBox="0 0 8 5"><path d="M1 1l3 3 3-3" fill="none" stroke="#888"/></svg></div><div>Full Time</div></div>
    <div class="row"><div class="job-title"><span class="check"></span>Software Engineer</div><div>Country</div><div>0 -1</div><div>$ 20000</div><div class="skills">HTML Javascript <svg width="8" height="5" viewBox="0 0 8 5"><path d="M1 1l3 3 3-3" fill="none" stroke="#888"/></svg></div><div>Full Time</div></div>
    <div class="row"><div class="job-title"><span class="check"></span>Software Engineer</div><div>Country</div><div>0 -1</div><div>$ 20000</div><div class="skills">HTML Javascript <svg width="8" height="5" viewBox="0 0 8 5"><path d="M1 1l3 3 3-3" fill="none" stroke="#888"/></svg></div><div>Full Time</div></div>
    <div class="row"><div class="job-title"><span class="check"></span>Software Engineer</div><div>Country</div><div>0 -1</div><div>$ 20000</div><div class="skills">HTML Javascript <svg width="8" height="5" viewBox="0 0 8 5"><path d="M1 1l3 3 3-3" fill="none" stroke="#888"/></svg></div><div>Full Time</div></div>

    <div class="subscribe-bar">
      <span>Get new jobs for these filters:</span>
      <span class="subscribe-email">Your email address</span>
      <span class="frequency"><span class="radio on"></span>Weekly</span>
      <span class="frequency"><span class="radio"></span>Monthly</span>
      <span class="subscribe-button">SUBSCRIBE</span>
    </div>
  </section>

  <div class="add-button" aria-label="Post a job">
    <svg width="20" height="20" viewBox="0 0 20 20"><path d="M10 1v18M1 10h18" stroke="#fff" stroke-width="2"/></svg>
  </div>

  <footer class="site-footer">Copyright © website address I All Rights Reaserved</footer>
</body>
</html>
```